Plainly Query Rowan Consulting needs a new and exciting customer online experience (Webpage)

Plainly Query Rowan is a new and exciting IT and Telecoms business. We aim to help business with all of its technology needs.

The business has only been around less than 12 months and a page was developed to give some online presence, but now its time for a refresh. The page is very bland and boring. It needs some creative zing to give it that pop whilst maintaining a professional appeal.

Our current page can be found at www.plainlyqueryrowan.com.au

I have included below some of our current marketing. I've included our business cards and some of messages on hold we are running.

Target Market(s)

Small to medium business, small enterprise

Industry/Entity Type

Business

Number of Pages Required

5+ page

Font styles to use
Sans Serif

Requirements
Must have
• The page must have some colour. IT and Telecoms can be mundane and boring. We want people to be engaged in their IT and Telecoms. We want them to feel as passionate about their IT and Telecoms as we do.
• It must have the following pages: Home, About Us, Services We provide, Contact Us and our Blog Page.
• The contact us should have an option to complete an online form which is delivered to our enquiries email.
• We would also like to have our social media links for Facebook, LinkedIn and Google plus. The pages must also contain a link to our privacy policy located near the bottom of the page

```html
<!DOCTYPE html>
<html lang="en">
<head>
<meta charset="utf-8">
<title>Plainly Query Rowan Consulting</title>
<link rel="stylesheet" href="https://fonts.googleapis.com/css2?family=Raleway:wght@300;400;600;700&display=swap">
<style>
  :root {
    --ink: #1d1d2c;
    --accent: #2bb3e8;
    --hero: #46426b;
    --band: #f2f2f2;
    --green: #9bc13c;
    --red: #d81a37;
    --purple: #46426b;
    --muted: #8d8d96;
    --footer: #15202b;
    --footer-deep: #101923;
    --footer-text: #7d8793;
    --white: #ffffff;
  }
  * { margin: 0; padding: 0; box-sizing: border-box; }
  html, body { width: 992px; height: 1200px; overflow: hidden; }
  body { font-family: "Raleway", sans-serif; color: var(--ink); background: var(--white); position: relative; }

  .site-header { position: absolute; top: 0; left: 0; width: 992px; height: 65px; background: var(--white); }
  .brand { position: absolute; left: 60px; top: 14px; display: flex; align-items: center; gap: 8px; }
  .brand-dot { width: 14px; height: 14px; border-radius: 50%; background: var(--accent); }
  .brand-name { font-size: 12px; font-weight: 600; line-height: 1.2; color: var(--ink); }
  .main-nav { position: absolute; right: 64px; top: 0; height: 65px; display: flex; }
  .main-nav a { display: flex; align-items: center; padding: 0 14px; font-size: 13px; color: var(--ink); text-decoration: none; height: 65px; position: relative; }
  .main-nav a.is-active { background: var(--accent); color: var(--white); padding: 0 16px; }
  .main-nav a.is-active::after { content: ""; position: absolute; bottom: 0; left: 50%; margin-left: -5px; border: 5px solid transparent; border-bottom-color: var(--white); }

  .hero { position: absolute; top: 65px; left: 0; width: 992px; height: 407px; background: var(--hero); color: var(--white); }
  .hero-title { position: absolute; left: 60px; top: 88px; font-size: 54px; font-weight: 300; line-height: 63px; }
  .hero-sub { position: absolute; left: 60px; top: 217px; font-size: 25px; font-weight: 400; }
  .hero-tagline { position: absolute; left: 60px; top: 267px; font-size: 14px; font-weight: 400; }
  .btn-outline { position: absolute; left: 60px; top: 315px; width: 61px; height: 34px; border: 1px solid var(--white); color: var(--white); font-size: 12px; font-weight: 600; display: flex; align-items: center; justify-content: center; }
  .hero-visual { position: absolute; left: 505px; top: 90px; width: 424px; height: 250px; }
  .slider-dots { position: absolute; top: 385px; left: 456px; display: flex; gap: 4px; }
  .slider-dots span { width: 22px; height: 3px; background: #8a879f; }
  .slider-dots span.is-current { background: #111; }

  .intro-band { position: absolute; top: 472px; left: 0; width: 992px; height: 106px; background: var(--band); }
  .intro-title { position: absolute; left: 133px; top: 26px; font-size: 28px; font-weight: 400; letter-spacing: 0.5px; color: var(--ink); }
  .intro-sub { position: absolute; left: 134px; top: 59px; font-size: 16px; font-weight: 400; color: var(--accent); }
  .btn-light { position: absolute; left: 793px; top: 38px; width: 60px; height: 34px; background: var(--white); font-size: 12px; font-weight: 600; display: flex; align-items: center; justify-content: center; }

  .features { position: absolute; top: 652px; left: 60px; display: flex; gap: 22px; }
  .feature { width: 274px; }
  .feature-art { width: 274px; height: 163px; }
  .feature-art.green { background: linear-gradient(135deg, #a2c63f, #8fb535); }
  .feature-art.red { background: linear-gradient(135deg, #dd1f3b, #cc1631); }
  .feature-art.purple { background: linear-gradient(135deg, #4b4772, #3f3b63); }
  .feature-title { margin-top: 9px; font-size: 13px; font-weight: 700; text-transform: uppercase; color: var(--ink); }
  .feature-text { margin-top: 14px; font-size: 11.5px; line-height: 21px; color: var(--muted); }
  .feature-text a { color: var(--accent); font-weight: 600; text-decoration: none; border-bottom: 1px solid var(--accent); }

  .site-footer { position: absolute; top: 962px; left: 0; width: 992px; height: 193px; background: var(--footer); color: var(--white); }
  .footer-marker { position: absolute; top: 0; left: 466px; width: 54px; height: 3px; background: var(--accent); }
  .footer-brand { position: absolute; left: 70px; top: 48px; display: flex; align-items: center; gap: 8px; }
  .footer-brand .brand-name { color: var(--white); }
  .footer-col { position: absolute; top: 34px; }
  .footer-col h3 { font-size: 13.5px; font-weight: 700; text-transform: uppercase; margin-bottom: 12px; }
  .footer-col p, .footer-col li { font-size: 11px; color: var(--footer-text); line-height: 21px; }
  .col-tweets { left: 282px; }
  .col-posts { left: 504px; }
  .col-posts ul { list-style: none; }
  .col-posts li::before { content: "\2022"; margin-right: 5px; }
  .col-contact { left: 727px; }
  .contact-line { display: flex; align-items: center; gap: 12px; height: 23px; }
  .contact-line svg { width: 12px; height: 12px; flex: none; }
  .legal-bar { position: absolute; top: 1155px; left: 0; width: 992px; height: 45px; background: var(--footer-deep); }
  .legal-bar p { position: absolute; left: 60px; top: 17px; font-size: 10.5px; color: #6b7480; }
</style>
</head>
<body>
  <header class="site-header">
    <div class="brand">
      <span class="brand-dot"></span>
      <span class="brand-name">Plainly Query Rowan<br>Consulting</span>
    </div>
    <nav class="main-nav">
      <a class="is-active" href="#">Home</a>
      <a href="#">About Us</a>
      <a href="#">Our Services</a>
      <a href="#">Contact Us</a>
      <a href="#">Blog</a>
    </nav>
  </header>

  <section class="hero">
    <h1 class="hero-title">PLAINLY QUERY<br>ROWAN</h1>
    <p class="hero-sub">consulting</p>
    <p class="hero-tagline">Making IT and Telecommunications simple for business.</p>
    <span class="btn-outline">Ask!</span>
    <svg class="hero-visual" viewBox="0 0 424 250" role="img" aria-label="Laptop showing a flat business illustration with charts, calendar and documents">
      <defs>
        <linearGradient id="screenTone" x1="0" y1="0" x2="1" y2="1">
          <stop offset="0" stop-color="#a3c43f"/>
          <stop offset="1" stop-color="#8fb436"/>
        </linearGradient>
      </defs>
      <rect x="40" y="0" width="346" height="228" rx="8" fill="#1a1a1f"/>
      <rect x="52" y="12" width="322" height="206" fill="url(#screenTone)"/>
      <rect x="0" y="228" width="424" height="14" rx="4" fill="#c9cbd0"/>
    </svg>
    <div class="slider-dots"><span class="is-current"></span><span></span><span></span></div>
  </section>

  <section class="intro-band">
    <h2 class="intro-title">MAKING IT AND TELECOMMUNICATIONS</h2>
    <p class="intro-sub">SIMPLE FOR BUSINESS</p>
    <span class="btn-light">Ask!</span>
  </section>

  <section class="features">
    <article class="feature">
      <div class="feature-art green" role="img" aria-label="Illustration of tools surrounded by technology icons"></div>
      <h3 class="feature-title">What can we help with</h3>
      <p class="feature-text">Cras accumsan pellentesque dignissim. Duis volutpat odio cursus. Vivamus rhoncus, arcu ac faucibus laoreet, lorem tellus varius lectus... <a href="#">read more</a></p>
    </article>
    <article class="feature">
      <div class="feature-art red" role="img" aria-label="Illustration of a piggy bank with clocks and coins"></div>
      <h3 class="feature-title">How can we help</h3>
      <p class="feature-text">Cras accumsan pellentesque dignissim. Duis volutpat odio cursus. Vivamus rhoncus, arcu ac faucibus laoreet, lorem tellus varius lectus... <a href="#">read more</a></p>
    </article>
    <article class="feature">
      <div class="feature-art purple" role="img" aria-label="Illustration of a handshake with business icons"></div>
      <h3 class="feature-title">Why not contact us</h3>
      <p class="feature-text">Cras accumsan pellentesque dignissim. Duis volutpat odio cursus. Vivamus rhoncus, arcu ac faucibus laoreet, lorem tellus varius lectus... <a href="#">read more</a></p>
    </article>
  </section>

  <footer class="site-footer">
    <span class="footer-marker"></span>
    <div class="footer-brand">
      <span class="brand-dot"></span>
      <span class="brand-name">Plainly Query Rowan<br>Consulting</span>
    </div>
    <div class="footer-col col-tweets">
      <h3>Latest Tweets</h3>
      <p>Loading...</p>
    </div>
    <div class="footer-col col-posts">
      <h3>Recent Posts</h3>
      <ul>
        <li>Nullam nisl nibh, porta et nunc vel</li>
        <li>Nullam nisl nibh, porta et nunc vel</li>
        <li>Nullam nisl nibh, porta et nunc vel</li>
        <li>Nullam nisl nibh, porta et nunc vel</li>
      </ul>
    </div>
    <div class="footer-col col-contact">
      <h3>Contact</h3>
      <p class="contact-line">
        <svg viewBox="0 0 12 12"><path d="M6 0.5a4 4 0 0 0-4 4c0 3 4 7 4 7s4-4 4-7a4 4 0 0 0-4-4z" fill="#2bb3e8"/><circle cx="6" cy="4.5" r="1.4" fill="#15202b"/></svg>
        214 Harbour Lane Seacliff East SA
      </p>
      <p class="contact-line">
        <svg viewBox="0 0 12 12"><path d="M1 4c0-2 2-3 5-3s5 1 5 3l-2 1-1-2H4L3 5z" fill="#2bb3e8"/><rect x="2" y="6" width="8" height="5" rx="1" fill="#2bb3e8"/></svg>
        (08) 7000 3186
      </p>
      <p class="contact-line">
        <svg viewBox="0 0 12 12"><rect x="0.5" y="2" width="11" height="8" fill="#2bb3e8"/><path d="M0.5 2l5.5 4 5.5-4" fill="none" stroke="#15202b" stroke-width="1"/></svg>
        enquiries@plainlyqueryrowan.com.au
      </p>
    </div>
  </footer>

  <div class="legal-bar"><p>2014 Plainly Query Rowan. All rights reserved.</p></div>
</body>
</html>
```